Vodka label, brand name: LATE BIRCH

We are looking for a vodka label design, which will print on paper or plastic (not a bottle printing)

We are small distilling company: Ferncliff Distillery. Located in Toronto, Canada. Our business is small batches of handcrafted very smooth vodka production. 40% abv. Made from cane sugar and spring water.

Our audience pretty mach everyone who consume vodka/alcohol, we are not targeting any specific group.

Back label should have barcode, government warning and this text:

Our vodka is handmade in small batches to the highest standards befitting the true vodka perfectionist. We use silk filtering process for exceptional purity, clarity, and smoothness. It is distilled 6 times from the finest organic cane sugar using only the best Canadian spring water. Discover the smooth, clear taste for yourself.
Distilled and Bottled by
Ferncliff Distillery Inc.
Toronto, Canada

Government Warning: In accordance to the Surgeon General, women should not drink alcoholic beverages during pregnancy because of the risk of birth defects. Consumption of alcoholic beverages impairs your ability to drive a car or operate machinery and may cause health problems.

Size of the bottle as follows (see example in the attachment) :
Volume: 750ml
Total height: 330mm
Body diameter: 77mm
Closure: Bar Top
Silver synthetic cork

Target Market(s)

Colors

Designer to choose colors to be used in the design.

Requirements
Must have
• Incorporate the name: LATE BIRCH
• Incorporate: DISTILLED FROM ORGANIC CANE SUGAR
• Back bottle label should have barcode, government warning and this text:
• Our vodka is handmade in small batches to the highest standards befitting the true vodka perfectionist. We use silk filtering process for exceptional purity, clarity, and smoothness. It is distilled 6 times from the finest organic cane sugar using only the best Canadian spring water. Discover the smooth, clear taste for yourself.
• Distilled and Bottleb by
• Ferncliff Distillery Inc.
• Toronto, Canada
• Government Warning: In accordance to the Surgeon General, women should not drink alcoholic beverages during pregnancy because of the risk of birth defects. Consumption of alcoholic beverages impairs your ability to drive a car or operate machinery and may cause health problems.
Nice to have
• 1) To show in wording or design it was Handmade
• 2) To show in wording or design it was made with Natural Spring Water
• To show in wording or design it was made in small batches
• 3) To show in wording or design it was made local in Toronto, Canada
• "The Six" "The 6ix"- is the nick name of city of Toronto that's just for designer to consider and not mandatory to implement on design
Should not have
• We try to lower cost of printing , so design should be for digital printing without Gold, Silver or any other color which requires foil application on label and will increase cost of printing.
• No copy paste from internet images. Such designs will be ignored and reported to website admin. Authentic design work only.
• Please try not to use clock or any related to that images. Its nothing to do with clock, its too naive to show 6 pm on the watches in your design. Its could be time of the day (evening), after work, the six as nick name of Toronto. But not clock or watches .

```html
<!DOCTYPE html>
<html lang="en">
<head>
<meta charset="utf-8">
<title>Late Birch Vodka Label</title>
<link href="https://fonts.googleapis.com/css2?family=Arimo:wght@400&family=Inter:wght@200&family=Oswald:wght@600&display=swap" rel="stylesheet">
<style>
  :root {
    --red: #e8000d;
    --white: #ffffff;
    --paper-dark: #d3d3d3;
    --paper-light: #fbfbfb;
    --lettering-tint: rgba(232, 0, 13, 0.14);
  }
  html, body {
    margin: 0;
    padding: 0;
    overflow: hidden;
    background: var(--white);
  }
  .label {
    position: relative;
    width: 941px;
    height: 1200px;
    overflow: hidden;
    background: var(--white);
    font-family: "Arimo", Arial, sans-serif;
    color: var(--red);
  }
  .front-panel {
    position: absolute;
    left: 0; top: 0;
    width: 941px; height: 901px;
    background: linear-gradient(90deg, var(--paper-dark) 0%, var(--paper-light) 100%);
  }
  .foot-band {
    position: absolute;
    left: 0; top: 1022px;
    width: 941px; height: 178px;
    background: linear-gradient(90deg, var(--paper-dark) 0%, var(--paper-light) 100%);
  }
  .brand-band {
    position: absolute;
    left: 512px; top: 0;
    width: 227px; height: 756px;
    background: var(--red);
  }
  .brand-mark {
    position: absolute;
    left: 604px; top: 48px;
  }
  .brand-name {
    position: absolute;
    left: 579px; top: 690px;
    width: 520px;
    height: 90px;
    line-height: 90px;
    transform: rotate(-90deg);
    transform-origin: top left;
    text-align: center;
    font-family: "Inter", Arial, sans-serif;
    font-weight: 200;
    font-size: 74px;
    letter-spacing: 3px;
    color: var(--white);
    white-space: nowrap;
  }
  .story {
    position: absolute;
    left: 768px; top: 750px;
    width: 700px;
    height: 150px;
    transform: rotate(-90deg);
    transform-origin: top left;
    margin: 0;
    font-size: 15px;
    line-height: 36px;
  }
  .lettering {
    position: absolute;
    left: 52px; top: 148px;
    width: 382px; height: 392px;
    background: linear-gradient(160deg, var(--lettering-tint), rgba(232, 0, 13, 0.06));
  }
  .warning {
    position: absolute;
    left: 140px; top: 605px;
    width: 342px;
    margin: 0;
    text-align: right;
    font-size: 15.3px;
    line-height: 21.5px;
  }
  .producer {
    position: absolute;
    left: 60px; top: 786px;
    margin: 0;
    font-size: 23.5px;
    line-height: 31px;
  }
  .claim {
    position: absolute;
    left: 370px; top: 802px;
    width: 350px;
    margin: 0;
    text-align: center;
    font-family: "Oswald", "Arial Narrow", sans-serif;
    font-weight: 600;
    font-size: 22px;
    line-height: 33px;
    letter-spacing: 0.3px;
  }
  .specs {
    position: absolute;
    right: 46px; top: 795px;
    margin: 0;
    text-align: right;
    font-size: 25px;
    line-height: 38px;
  }
  .leaf {
    position: absolute;
    left: 430px; top: 1062px;
    width: 94px; height: 94px;
    border-radius: 8px;
    background: var(--red);
  }
</style>
</head>
<body>
<main class="label">
  <div class="front-panel"></div>
  <div class="foot-band"></div>

  <div class="lettering" role="img" aria-label="Hand lettered script reading Hand made Vodka"></div>

  <p class="warning">Government Warning:<br>In accordance to the Surgeon General,<br>women should not drink alcoholic beverages<br>during pregnancy because of the risk of birth<br>defects. Consumption of alcoholic beverages<br>impairs your ability to drive a car or operate<br>machinery and may cause health problems.</p>

  <div class="brand-band"></div>
  <svg class="brand-mark" width="96" height="96" viewBox="0 0 96 96" aria-hidden="true">
    <circle cx="48" cy="48" r="45" fill="none" stroke="#ffffff" stroke-width="3"/>
  </svg>
  <div class="brand-name">LATE BIRCH</div>

  <p class="story">Our vodka is handmade in small batches to the highest standards<br>befitting the true vodka perfectionist. We use silk filtering process for exceptional purity,<br>clarity, and smoothness. It is distilled 6 times from the finest organic cane sugar using only the<br>best Canadian spring water. Discover the smooth, clear taste for yourself.</p>

  <p class="producer">Distilled and Bottled by<br>Ferncliff Distillery<br>Inc.Toronto, Canada</p>
  <p class="claim">DISTILLED FROM ORGANIC<br>CANE SUGAR</p>
  <p class="specs">40% abv<br>750ml</p>

  <div class="leaf" role="img" aria-label="Red maple leaf"></div>
</main>
</body>
</html>
```